Design Business Card CORAL TIDE MOWING

We have attached a copy of our Logo, we like a business card designed with logo and mobile phone number on one side that stands out maybe gloss and on the other side it can have the services we do small picture of our logo name number, I have attached an idea to this that I have seen online, this is a business owned by a woman so we like pinks black and navy
Our logo is attached in pdf
Target Market(s)
Home owners that need lawns mowed
Industry/Entity Type
Lawns and gardens
Contact Information for Business Card
Logo business Owner name Dorinda Pask mobile number 0417296054
Font styles to use
Look and feel
Each slider illustrates characteristics of the customer's brand and the style your logo design should communicate.

```html
<!DOCTYPE html>
<html lang="en">
<head>
<meta charset="utf-8">
<title>Coral Tide Mowing – Business Card</title>
<link rel="stylesheet" href="https://fonts.googleapis.com/css2?family=Saira:ital,wght@0,800;1,800;1,900&display=swap">
<style>
  :root {
    --page-bg: #1b2420;
    --pink-light: #fb74cf;
    --pink-mid: #ec56b6;
    --pink-deep: #c62b7c;
    --ink: #111111;
    --white: #ffffff;
    --grass-dark: #0c0a0c;
  }
  * { box-sizing: border-box; margin: 0; padding: 0; }
  html, body {
    width: 1200px;
    height: 900px;
    overflow: hidden;
    background: var(--page-bg);
  }
  .canvas {
    position: relative;
    width: 1200px;
    height: 900px;
    display: flex;
    flex-direction: column;
    align-items: center;
    justify-content: center;
    gap: 28px;
  }
  .card {
    position: relative;
    width: 720px;
    height: 400px;
    overflow: hidden;
    background: linear-gradient(180deg, var(--pink-light) 0%, var(--pink-mid) 40%, var(--pink-deep) 75%);
    box-shadow: 0 18px 40px rgba(0, 0, 0, 0.55);
  }
  .grass-band {
    position: absolute;
    left: 0;
    right: 0;
    bottom: 0;
    height: 110px;
    background: linear-gradient(180deg,
      rgba(12, 10, 12, 0) 0%,
      rgba(12, 10, 12, 0.55) 30%,
      rgba(12, 10, 12, 0.92) 55%,
      var(--grass-dark) 100%);
  }
  .brand {
    position: absolute;
    display: flex;
    align-items: center;
  }
  .brand-mark {
    flex: none;
    border-radius: 50%;
    background: var(--ink);
  }
  .brand-name {
    font-family: "Saira", sans-serif;
    font-weight: 800;
    color: var(--ink);
    line-height: 0.95;
    letter-spacing: 0.5px;
  }
  .card-front .brand {
    left: 50%;
    top: 62px;
    transform: translateX(-50%);
    gap: 22px;
  }
  .card-front .brand-mark { width: 150px; height: 150px; }
  .card-front .brand-name { font-size: 64px; white-space: nowrap; }

  .card-back .brand {
    left: 30px;
    top: 100px;
    gap: 14px;
  }
  .card-back .brand-mark { width: 110px; height: 110px; }
  .card-back .brand-name { font-size: 42px; white-space: nowrap; }

  .divider {
    position: absolute;
    left: 345px;
    top: 90px;
    width: 2px;
    height: 200px;
    background: var(--white);
  }
  .contact {
    position: absolute;
    left: 380px;
    top: 112px;
    color: var(--white);
    font-family: "Saira", sans-serif;
  }
  .owner-name {
    font-style: italic;
    font-weight: 900;
    font-size: 36px;
    letter-spacing: 1.5px;
    line-height: 1;
    text-transform: uppercase;
  }
  .owner-role {
    font-style: italic;
    font-weight: 800;
    font-size: 20px;
    margin-top: 2px;
  }
  .phone-row {
    display: flex;
    align-items: center;
    gap: 16px;
    margin-top: 40px;
  }
  .phone-icon { width: 40px; height: 40px; flex: none; }
  .phone-number {
    font-style: italic;
    font-weight: 900;
    font-size: 40px;
    letter-spacing: 1px;
    line-height: 1;
  }
</style>
</head>
<body>
<main class="canvas">
  <section class="card card-front" aria-label="Business card front">
    <div class="brand">
      <span class="brand-mark"></span>
      <span class="brand-name">CORAL TIDE<br>MOWING</span>
    </div>
    <div class="grass-band" role="img" aria-label="Dark grass silhouette along the bottom edge"></div>
  </section>

  <section class="card card-back" aria-label="Business card back">
    <div class="brand">
      <span class="brand-mark"></span>
      <span class="brand-name">CORAL<br>TIDE<br>MOWING</span>
    </div>
    <div class="divider"></div>
    <div class="contact">
      <p class="owner-name">Dorinda Pask</p>
      <p class="owner-role">Owner</p>
      <div class="phone-row">
        <svg class="phone-icon" viewBox="0 0 40 40" aria-hidden="true">
          <circle cx="20" cy="20" r="20" fill="#ffffff"/>
          <path d="M14.5 10.5c.8-.4 1.7-.1 2.1.6l2 3.4c.4.7.2 1.6-.4 2.1l-1.5 1.2c.9 2.2 2.6 4 4.8 5l1.2-1.5c.5-.6 1.4-.8 2.1-.4l3.4 2c.7.4 1 1.3.6 2.1l-1 2c-.6 1.2-2 1.8-3.3 1.4-6-1.8-10.4-6.3-12.2-12.3-.4-1.3.2-2.7 1.4-3.3z" fill="#e34fae"/>
          <path d="M22 11a7 7 0 0 1 7 7M22 14.5a3.5 3.5 0 0 1 3.5 3.5" stroke="#e34fae" stroke-width="1.8" fill="none" stroke-linecap="round"/>
        </svg>
        <span class="phone-number">0417296054</span>
      </div>
    </div>
    <div class="grass-band" role="img" aria-label="Dark grass silhouette along the bottom edge"></div>
  </section>
</main>
</body>
</html>
```